Business Card Design Project

i have the logo designed.
I require designs for the managing director and the general manager.
we need space for email, and a mobile number.
any other cool stuff/design you guys just let me see what you got.
The managing director card could be black, minimalist, and the cards for the rest of the company could be using the green logo.
it has to impress. transportation market is fragmented, we want to appear professional and sophisticated.
Md: Tarek bani rahim
General manager: omer rahim
clients: procurement heads of contracting companies
Business

```html
<!DOCTYPE html>
<html lang="en">
<head>
<meta charset="utf-8">
<title>Velora Business Cards</title>
<link rel="stylesheet" href="https://fonts.googleapis.com/css2?family=Roboto+Condensed:wght@400;700&display=swap">
<style>
  :root {
    --board-light: #f7f7f7;
    --board-dark: #d6d6d6;
    --frame: #ffffff;
    --director-black: #121212;
    --brand-green: #2e8a14;
    --bright-green: #4fb014;
    --ink: #111111;
    --paper: #ffffff;
    --soft-white: #e8e8e8;
    --faint-on-black: rgba(79, 176, 20, 0.16);
    --faint-on-white: rgba(46, 138, 20, 0.12);
  }
  * { box-sizing: border-box; margin: 0; padding: 0; }
  html, body { width: 900px; height: 1200px; overflow: hidden; }
  body {
    position: relative;
    background: radial-gradient(ellipse at 50% 40%, var(--board-light) 0%, var(--board-dark) 100%);
    font-family: "Roboto Condensed", "Arial Narrow", sans-serif;
    color: var(--ink);
  }
  .card-frame {
    position: absolute;
    background: var(--frame);
    box-shadow: 0 3px 8px rgba(0, 0, 0, 0.3);
  }
  .card {
    position: absolute;
    overflow: hidden;
  }
  .brand-name {
    position: absolute;
    font-weight: 700;
    letter-spacing: 1px;
    line-height: 1;
    white-space: nowrap;
  }
  .card-details {
    position: absolute;
    line-height: 1.05;
  }
  .card-details .holder-name { font-size: 20px; }
  .card-details .holder-role { font-size: 12px; letter-spacing: 1px; text-transform: uppercase; margin-bottom: 4px; }
  .card-details .detail-line { font-size: 13px; letter-spacing: -0.2px; }

  /* Managing Director, front (black) */
  .director-front-frame { left: 3px; top: 12px; width: 488px; height: 300px; }
  .director-front {
    left: 18px; top: 15px; width: 452px; height: 266px;
    background: var(--director-black);
  }
  .director-front .brand-name { left: 125px; top: 135px; font-size: 82px; color: var(--bright-green); }

  /* Managing Director, back (black) */
  .director-back-frame { left: 358px; top: 333px; width: 538px; height: 335px; }
  .director-back {
    left: 17px; top: 18px; width: 503px; height: 297px;
    background: var(--director-black);
    border-top: 2px solid var(--bright-green);
    border-bottom: 2px solid var(--bright-green);
  }
  .director-back .brand-watermark { left: 24px; top: 200px; font-size: 64px; color: var(--faint-on-black); }
  .director-back .brand-name.brand-main { left: 285px; top: 40px; font-size: 34px; color: var(--bright-green); }
  .director-back .card-details { left: 290px; top: 82px; color: var(--soft-white); }

  /* General Manager, front (white) */
  .manager-front-frame { left: 3px; top: 735px; width: 455px; height: 278px; }
  .manager-front {
    left: 18px; top: 15px; width: 420px; height: 248px;
    background: var(--paper);
    box-shadow: inset 0 0 12px 4px rgba(0, 0, 0, 0.9);
  }
  .manager-front .brand-name { left: 86px; top: 128px; font-size: 78px; color: var(--brand-green); }

  /* General Manager, back (white) */
  .manager-back-frame { left: 470px; top: 743px; width: 427px; height: 265px; }
  .manager-back {
    left: 13px; top: 19px; width: 400px; height: 232px;
    background: var(--paper);
    border-top: 2px solid var(--ink);
    border-bottom: 2px solid var(--ink);
  }
  .manager-back .brand-watermark { left: 18px; top: 158px; font-size: 50px; color: var(--faint-on-white); }
  .manager-back .brand-name.brand-main { left: 222px; top: 18px; font-size: 28px; color: var(--brand-green); }
  .manager-back .card-details { left: 230px; top: 52px; }
  .manager-back .card-details .holder-name { font-size: 18px; }
  .manager-back .card-details .holder-role { font-size: 11px; }
  .manager-back .card-details .detail-line { font-size: 12px; }
</style>
</head>
<body>

  <div class="card-frame director-front-frame">
    <div class="card director-front">
      <span class="brand-name">Velora</span>
    </div>
  </div>

  <div class="card-frame director-back-frame">
    <div class="card director-back">
      <span class="brand-name brand-watermark" aria-hidden="true">Velora</span>
      <span class="brand-name brand-main">Velora</span>
      <div class="card-details">
        <p class="holder-name">Tarek bani rahim</p>
        <p class="holder-role">Managing Director</p>
        <p class="detail-line">48 Marlow Rd</p>
        <p class="detail-line">Kingsmead</p>
        <p class="detail-line">Eastford</p>
        <p class="detail-line">4100</p>
        <p class="detail-line">Tel:(031)-555-0142</p>
        <p class="detail-line">Fax:(031)-555-0143</p>
        <p class="detail-line">Mobile:(082)-555-0178</p>
        <p class="detail-line">tarek@velora-freight.com</p>
      </div>
    </div>
  </div>

  <div class="card-frame manager-front-frame">
    <div class="card manager-front">
      <span class="brand-name">Velora</span>
    </div>
  </div>

  <div class="card-frame manager-back-frame">
    <div class="card manager-back">
      <span class="brand-name brand-watermark" aria-hidden="true">Velora</span>
      <span class="brand-name brand-main">Velora</span>
      <div class="card-details">
        <p class="holder-name">omer rahim</p>
        <p class="holder-role">General Manager</p>
        <p class="detail-line">48 Marlow Rd</p>
        <p class="detail-line">Kingsmead</p>
        <p class="detail-line">Eastford</p>
        <p class="detail-line">4100</p>
        <p class="detail-line">Tel:(031)-555-0142</p>
        <p class="detail-line">Fax:(031)-555-0143</p>
        <p class="detail-line">Mobile:(082)-555-0179</p>
        <p class="detail-line">omer@velora-freight.com</p>
      </div>
    </div>
  </div>

</body>
</html>
```